New locally owned rental company needs a flyer to circulate

Need flyer with logo, phone# and address. We rent cars to anyone with driver's license and proper insurance. Rates as low as $50/day. Can offer compact cars, mid-size and full size sedans. Also SUV's.

```html
<!DOCTYPE html>
<html lang="en">
<head>
<meta charset="utf-8">
<title>DriveSoon Car &amp; Van Rental Flyer</title>
<link rel="stylesheet" href="https://fonts.googleapis.com/css2?family=Archivo+Black&family=Fira+Sans+Condensed:wght@500;600&family=Fira+Sans:wght@400;800&display=swap">
<style>
  :root {
    --brand-blue: #0054ad;
    --brand-green: #2db256;
    --ink: #111111;
    --text-grey: #3b3b3b;
    --paper: #ffffff;
    --photo-dark: #4a4d50;
    --photo-light: #8a8e91;
  }
  * { margin: 0; padding: 0; box-sizing: border-box; }
  html, body { width: 927px; height: 1200px; overflow: hidden; background: var(--paper); }
  .flyer { position: relative; width: 927px; height: 1200px; background: var(--paper); font-family: "Fira Sans", sans-serif; }
  .backdrop { position: absolute; inset: 0; }

  .brand { position: absolute; left: 63px; top: 50px; width: 420px; text-align: center; }
  .brand-name { font-family: "Archivo Black", sans-serif; font-size: 64px; line-height: 1; color: var(--brand-blue); letter-spacing: -2px; }
  .brand-tagline { margin-top: 10px; font-family: "Fira Sans", sans-serif; font-weight: 800; font-size: 22px; letter-spacing: 11px; color: var(--ink); }

  .headline { position: absolute; font-family: "Archivo Black", sans-serif; line-height: 1; white-space: nowrap; transform-origin: left top; }
  .headline-rental { top: 207px; left: 68px; font-size: 101px; letter-spacing: -4px; color: var(--brand-blue); transform: scaleX(0.83); }
  .headline-cars { top: 291px; left: 57px; font-size: 145px; letter-spacing: -6px; color: var(--brand-green); transform: scaleX(0.8); }

  .fleet { position: absolute; left: 56px; top: 462px; width: 368px; font-family: "Fira Sans Condensed", sans-serif; font-weight: 500; text-align: center; }
  .fleet-compact { font-size: 49px; line-height: 1; color: var(--brand-blue); }
  .fleet-sedans { margin-top: 12px; height: 39px; border-radius: 7px; background: var(--brand-blue); color: var(--paper); font-size: 30px; line-height: 39px; }
  .fleet-suv { position: relative; margin-top: 8px; height: 48px; }
  .fleet-suv-bar { position: absolute; left: 47px; top: 6px; width: 116px; height: 38px; border-radius: 6px; background: var(--brand-green); }
  .fleet-suv-label { position: absolute; left: 180px; top: -4px; font-size: 60px; line-height: 1; color: var(--brand-green); }

  .rate { position: absolute; left: 611px; top: 291px; width: 260px; height: 280px; color: var(--paper); }
  .rate-title { position: absolute; left: 0; top: 0; font-family: "Archivo Black", sans-serif; font-size: 97px; line-height: 1; letter-spacing: -3px; white-space: nowrap; transform: scaleX(0.76); transform-origin: left top; }
  .rate-low { position: absolute; left: 0; top: 93px; width: 246px; height: 28px; }
  .rate-low-label { position: absolute; left: 3px; top: 0; font-family: "Archivo Black", sans-serif; font-size: 21px; letter-spacing: 6px; line-height: 28px; white-space: nowrap; }
  .rate-low-bar { position: absolute; left: 137px; top: 0; width: 108px; height: 28px; border-radius: 5px; background: var(--paper); }
  .rate-price { position: absolute; left: 0; top: 115px; font-family: "Archivo Black", sans-serif; font-size: 172px; line-height: 1; letter-spacing: -6px; white-space: nowrap; transform: scaleX(0.8); transform-origin: left top; }

  .vehicle-photo { position: absolute; left: 77px; top: 607px; width: 774px; height: 486px; }

  .contact { position: absolute; top: 1105px; display: flex; align-items: center; }
  .contact-phone { left: 82px; }
  .contact-address { left: 489px; }
  .contact-icon { flex: none; }
  .phone-number { margin-left: 24px; font-size: 25px; letter-spacing: 11px; color: var(--text-grey); }
  .street-address { margin-left: 20px; font-size: 21px; line-height: 1.3; font-style: normal; color: var(--text-grey); }
</style>
</head>
<body>
<main class="flyer">
  <svg class="backdrop" width="927" height="1200" viewBox="0 0 927 1200" aria-hidden="true">
    <path d="M512 176 C480 176 460 210 465 245 L505 513 L560 176 Z" fill="var(--brand-green)"/>
    <path d="M610 129 L927 129 L927 1027 Q927 1077 877 1077 L485 1077 Q434 1077 434 1025 L556 190 Q566 129 610 129 Z" fill="var(--brand-blue)"/>
  </svg>

  <header class="brand">
    <div class="brand-name">DriveSoon</div>
    <div class="brand-tagline">Car &amp; Van Rental</div>
  </header>

  <h1 class="headline headline-rental">RENTAL</h1>
  <h1 class="headline headline-cars">CARS!</h1>

  <section class="fleet">
    <p class="fleet-compact">COMPACT CARS</p>
    <p class="fleet-sedans">MID-SIZE &amp; FULL SEDANS</p>
    <div class="fleet-suv"><span class="fleet-suv-bar"></span><span class="fleet-suv-label">SUV’S</span></div>
  </section>

  <section class="rate">
    <p class="rate-title">RATES</p>
    <div class="rate-low"><span class="rate-low-label">LOW AS</span><span class="rate-low-bar"></span></div>
    <p class="rate-price">$50</p>
  </section>

  <svg class="vehicle-photo" role="img" aria-label="Photo of a grey mid-size SUV, front three-quarter view" viewBox="0 0 774 486">
    <defs>
      <linearGradient id="suvTone" x1="0" y1="0" x2="1" y2="1">
        <stop offset="0" stop-color="var(--photo-light)"/>
        <stop offset="1" stop-color="var(--photo-dark)"/>
      </linearGradient>
    </defs>
    <path d="M40 190 Q150 90 300 70 Q420 0 620 5 Q720 20 760 120 L774 330 Q700 460 560 440 L360 470 Q150 486 40 400 Q0 300 40 190 Z" fill="url(#suvTone)"/>
  </svg>

  <footer>
    <div class="contact contact-phone">
      <svg class="contact-icon" width="68" height="60" viewBox="0 0 68 60" aria-hidden="true">
        <ellipse cx="34" cy="50" rx="31" ry="8" fill="none" stroke="var(--brand-blue)" stroke-width="3"/>
        <path d="M26 4 h8 v14 h-5 v14 h5 v14 h-8 q-6 0 -6 -6 v-30 q0 -6 6 -6 Z" fill="var(--brand-blue)"/>
      </svg>
      <span class="phone-number">256-555-0142</span>
    </div>
    <div class="contact contact-address">
      <svg class="contact-icon" width="57" height="60" viewBox="0 0 57 60" aria-hidden="true">
        <ellipse cx="28" cy="50" rx="26" ry="8" fill="none" stroke="var(--brand-blue)" stroke-width="3"/>
        <path d="M28 48 L14 26 A16 16 0 1 1 42 26 Z" fill="var(--brand-blue)"/>
        <circle cx="28" cy="18" r="6" fill="var(--paper)"/>
      </svg>
      <address class="street-address">4870B Cedar Ridge Parkway<br>Huntsville, AL 35801</address>
    </div>
  </footer>
</main>
</body>
</html>
```